Etiketten für Fruchtaufstriche gesucht
Zielgruppe
Marmeladen, Fruchtaufstriche, Aufstriche
Aufgabenstellung
Im Etikett sollte das Logo 'Tildas blaue Wiese' (siehe Anlage) integriert sein. Gerne können dazu ein Kreis und Früchte gestaltet werden, das ist aber kein Muss. Das Etikett sollte aber eben grundsätzlich zum Logo passen. Größe: Höhe: max. 4cm; Breite: max. 7,5cm - 8cm
Wird auf verschiedenen Gläsern verwendet zwischen 220-430g für Fruchtaufstriche, deshalb die Maße.
Früchte (sollten jeweils in das Etikett einsetzbar sein und als jpg etc. mitgeliefert werden:
Apfel, Aprikose, Birne, Brombeere, Erdbeere, Heidelbeere, Himbeere, Johannisbeere( rot, schwarz, weiß), Kirsche, Kürbis, Mirabelle, Pfirsich, Quitte, Rharbarber, Stachelbeere, Tomate, Weintraube( grün, blau), Wildpflaume ('Kriacherl'), Zucchini, Zwetschge.
Sollten die Früchtebilder nicht mitgeliefert werden, ist ein Verweis auf entsprechende Fotodateien nötig.
Zutaten: Früchte, Gewürze, Zucker; Geliermittel: Citruspektin; Säuerungsmittel: Zitronensäure
Mengenangabe: 220g ( 4mm)
Bezeichnung: Fruchtaufstrich oder Gelee
Mindesthaltbarkeitsdatum
Beispiel: siehe Anhang (Aprikosenetikett)
Das Etikett muss so gestaltet sein, dass wir es auch ändern können (Adobe Indesign, etc.) und jeweils die passenden Fruchtbilder einfügen können; da ich mit AI arbeite, benötige ich eine bearbeitbare Adobe Indesign Datei

```html
<!DOCTYPE html>
<html lang="de">
<head>
<meta charset="utf-8">
<title>Tildas blaue Wiese – Etiketten</title>
<link rel="stylesheet" href="https://fonts.googleapis.com/css2?family=Yanone+Kaffeesatz:wght@300;400;600&family=Fira+Sans+Condensed:wght@400;500&display=swap">
<style>
  :root {
    --bg: #ffffff;
    --green: #7ab648;
    --ink: #222222;
    --apricot-band: #f6a183;
    --apricot-photo: linear-gradient(90deg, #e8876a, #f3b07a 30%, #f6c48e 60%, #e98a62);
    --apricot-ribbon: #ef7a3f;
    --rhubarb-band: #e1737f;
    --rhubarb-photo: linear-gradient(180deg, #c9585f, #e7a3a4 35%, #cf5a63 60%, #a63a44 85%, #2a1d1c);
    --rhubarb-ribbon: #e0245e;
    --currant-band: #f1cf6b;
    --currant-photo: linear-gradient(90deg, #5d6a2b, #c9b651 25%, #7a7a32 45%, #f3b52c 70%, #e59a1c 85%, #4d5a25);
    --currant-ribbon: #f2bf1d;
  }
  * { box-sizing: border-box; margin: 0; padding: 0; }
  html, body { width: 896px; height: 1200px; overflow: hidden; background: var(--bg); }
  body { position: relative; font-family: "Fira Sans Condensed", sans-serif; color: var(--ink); }

  .label {
    position: absolute;
    left: 261px;
    width: 375px;
    height: 195px;
    background: #fff;
    box-shadow: 6px 10px 14px rgba(0,0,0,0.22);
    overflow: hidden;
  }
  .label--apricot { top: 170px; }
  .label--rhubarb { top: 500px; }
  .label--currant { top: 830px; }

  .label__web {
    height: 27px;
    line-height: 27px;
    text-align: center;
    color: #fff;
    font-family: "Yanone Kaffeesatz", sans-serif;
    font-weight: 600;
    font-size: 12px;
    letter-spacing: 2.4px;
  }
  .label__photo { height: 62px; }
  .label--apricot .label__web { background: var(--apricot-band); }
  .label--apricot .label__photo { background: var(--apricot-photo); }
  .label--rhubarb .label__web { background: var(--rhubarb-band); }
  .label--rhubarb .label__photo { background: var(--rhubarb-photo); }
  .label--currant .label__web { background: var(--currant-band); }
  .label--currant .label__photo { background: var(--currant-photo); border-bottom: 4px solid var(--currant-band); }

  .label__brand {
    position: absolute;
    top: 92px; left: 0; right: 0;
    text-align: center;
    font-family: "Yanone Kaffeesatz", sans-serif;
    font-weight: 400;
    font-size: 23px;
    line-height: 26px;
    color: var(--green);
  }
  .label__type {
    position: absolute;
    top: 121px; left: 0; right: 0;
    text-align: center;
    font-family: "Yanone Kaffeesatz", sans-serif;
    font-size: 12px;
    line-height: 14px;
    letter-spacing: 2.6px;
    color: var(--green);
  }
  .label__variant {
    position: absolute;
    top: 137px; left: 0; right: 0;
    text-align: center;
    font-family: "Yanone Kaffeesatz", sans-serif;
    font-size: 12px;
    line-height: 14px;
    letter-spacing: 4px;
    color: var(--currant-ribbon);
  }
  .ribbon {
    position: absolute;
    left: 110px;
    width: 155px;
    height: 34px;
  }
  .label--apricot .ribbon, .label--rhubarb .ribbon { top: 148px; }
  .label--currant .ribbon { top: 154px; }
  .ribbon svg { position: absolute; inset: 0; }
  .ribbon__text {
    position: relative;
    display: block;
    text-align: center;
    white-space: nowrap;
    line-height: 34px;
    color: #fff;
    font-family: "Yanone Kaffeesatz", sans-serif;
    font-weight: 300;
    font-size: 25px;
    letter-spacing: 2.5px;
  }
  .ribbon__text--long {
    font-size: 22px;
    letter-spacing: 0.6px;
  }

  .label__facts {
    position: absolute;
    top: 97px;
    font-size: 8.6px;
    line-height: 13.6px;
    letter-spacing: -0.2px;
  }
  .label__facts--ingredients { left: 11px; }
  .label__facts--dates { left: 300px; }
  .label__weight {
    position: absolute;
    right: 14px; top: 166px;
    font-family: "Fira Sans Condensed", sans-serif;
    font-weight: 500;
    font-size: 15px;
  }
</style>
</head>
<body>

  <section class="label label--apricot">
    <div class="label__web">WWW.TILDAS-BLAUE-WIESE.DE</div>
    <div class="label__photo" role="img" aria-label="Foto reifer Aprikosen"></div>
    <div class="label__brand">Tildas blaue Wiese</div>
    <div class="label__type">FRUCHTAUFSTRICH</div>
    <div class="ribbon">
      <svg viewBox="0 0 155 34" preserveAspectRatio="none"><polygon points="0,0 155,0 146,17 155,34 0,34 9,17" fill="var(--apricot-ribbon)"/></svg>
      <span class="ribbon__text">APRIKOSE</span>
    </div>
  </section>

  <section class="label label--rhubarb">
    <div class="label__web">WWW.TILDAS-BLAUE-WIESE.DE</div>
    <div class="label__photo" role="img" aria-label="Foto frischer Rhabarberstangen"></div>
    <div class="label__brand">Tildas blaue Wiese</div>
    <div class="label__type">CHUTNEY</div>
    <div class="ribbon">
      <svg viewBox="0 0 155 34" preserveAspectRatio="none"><polygon points="0,0 155,0 146,17 155,34 0,34 9,17" fill="var(--rhubarb-ribbon)"/></svg>
      <span class="ribbon__text">RHARBABER</span>
    </div>
    <div class="label__facts label__facts--ingredients">Zutaten:<br>Früchte, Zucker<br>Säuerungsmittel:<br>Zitronensäure<br>Geliermittel:<br>Citruspektin</div>
    <div class="label__facts label__facts--dates">Mindestens haltbar:<br>01. 10. 2018<br>Hergestellt aus:<br>67 g Früchte<br>je 100g</div>
    <div class="label__weight">220g</div>
  </section>

  <section class="label label--currant">
    <div class="label__web">WWW.TILDAS-BLAUE-WIESE.DE</div>
    <div class="label__photo" role="img" aria-label="Foto weißer Johannisbeeren am Strauch"></div>
    <div class="label__brand">Tildas blaue Wiese</div>
    <div class="label__type">FRUCHTAUFSTRICH</div>
    <div class="label__variant">WEIßE</div>
    <div class="ribbon">
      <svg viewBox="0 0 155 34" preserveAspectRatio="none"><polygon points="0,0 155,0 146,17 155,34 0,34 9,17" fill="var(--currant-ribbon)"/></svg>
      <span class="ribbon__text ribbon__text--long">JOHANNISBEERE</span>
    </div>
    <div class="label__facts label__facts--ingredients">Zutaten:<br>Früchte, Zucker<br>Säuerungsmittel:<br>Zitronensäure<br>Geliermittel:<br>Citruspektin</div>
    <div class="label__facts label__facts--dates">Mindestens haltbar:<br>01. 10. 2018<br>Hergestellt aus:<br>67 g Früchte<br>je 100g</div>
    <div class="label__weight">220g</div>
  </section>

</body>
</html>
```